Alliance of Northern Urgent Care Scholars Poster Design

We need a pull up banner (specs attached) for the Alliance of Northern Urgent Care Scholars. This group enables emergency care researchers to conduct multi-center research or education studies, provide mentorship, create knowledge through research, support knowledge translation, and ultimately improve emergency patient care for all Canadians.

Font styles to use
Serif
Sans Serif

Colors

Designer to choose colors to be used in the design.

Requirements
Must have
• ANUS Logo
• BRTL Logo
• www.brtl.ca
• For more information contact: mdellow@brtl.ca
• Complimentary colours to the ANUS logo.
Nice to have
• Photos of the group (attached to brief) - our photos assuming they are the right resolution. Stock photos can potentially be used if these don't work.
Should not have
• No stock photos containing laboratory equipment.

```html
<!DOCTYPE html>
<html lang="en">
<head>
<meta charset="utf-8">
<title>Alliance of Northern Urgent Care Scholars – Pull-up Banner</title>
<link rel="stylesheet" href="https://fonts.googleapis.com/css2?family=Open+Sans:wght@400;600;700&display=swap">
<style>
  :root {
    --blue: #1a7fc3;
    --grey: #58585a;
    --grey-light: #6b6b6e;
    --red: #e3262b;
    --white: #ffffff;
    --photo-top: #b9b3a8;
    --photo-mid: #7f7369;
    --photo-low: #8b7a68;
  }
  * { margin: 0; padding: 0; box-sizing: border-box; }
  html, body { width: 1200px; height: 2707px; overflow: hidden; background: var(--white); }
  body { font-family: "Open Sans", Arial, sans-serif; color: var(--grey); }

  .banner { position: relative; width: 1200px; height: 2707px; background: var(--white); overflow: hidden; }

  .brand-lockup { position: absolute; left: 117px; top: 120px; height: 192px; display: flex; align-items: center; }
  .brand-mark { width: 24px; height: 24px; border-radius: 50%; background: var(--blue); margin-right: 16px; flex: none; }
  .brand-name { font-weight: 700; font-size: 64px; line-height: 1; color: var(--blue); }
  .brand-divider { width: 4px; height: 192px; background: var(--blue); margin: 0 32px 0 30px; flex: none; }
  .brand-title { font-weight: 600; font-size: 30px; line-height: 36px; color: var(--blue); width: 280px; }

  .partner-logo { position: absolute; left: 880px; top: 180px; height: 72px; display: flex; align-items: center; }
  .partner-logo .brand-mark { background: var(--red); }

  .mission { position: absolute; left: 117px; top: 452px; width: 930px; list-style: none; }
  .mission li { position: relative; padding-left: 83px; font-weight: 600; font-size: 50px; line-height: 67px; margin-bottom: 27px; }
  .mission li::before {
    content: ""; position: absolute; left: 0; top: 20px; width: 30px; height: 30px;
    border: 5px solid var(--blue); border-radius: 50%;
  }
  .mission .wrap { width: 830px; }

  .mission-close { position: absolute; left: 200px; top: 993px; width: 720px; font-weight: 600; font-size: 50px; line-height: 70px; }

  .contact { position: absolute; left: 200px; top: 1266px; }
  .contact-label { font-weight: 400; font-size: 42px; line-height: 56px; color: var(--grey-light); }
  .contact-email { font-weight: 700; font-size: 50px; line-height: 64px; color: var(--red); margin-top: 9px; }

  .group-photo {
    position: absolute; left: 0; top: 1480px; width: 1200px; height: 980px;
    background: linear-gradient(180deg, var(--photo-top) 0%, var(--photo-mid) 55%, var(--photo-low) 100%);
  }

  .site-url { position: absolute; left: 0; right: 0; top: 2490px; text-align: center; font-weight: 700; font-size: 64px; line-height: 84px; color: var(--blue); }
</style>
</head>
<body>
<main class="banner">
  <header>
    <div class="brand-lockup">
      <span class="brand-mark"></span>
      <span class="brand-name">ANUS</span>
      <span class="brand-divider"></span>
      <span class="brand-title">Alliance of Northern Urgent Care Scholars</span>
    </div>
    <div class="partner-logo">
      <span class="brand-mark"></span>
      <span class="brand-name">BRTL</span>
    </div>
  </header>

  <ul class="mission">
    <li>Multi-center research</li>
    <li>Education studies</li>
    <li>Provide mentorship</li>
    <li class="wrap">Create knowledge through research</li>
    <li>Support knowledge translation</li>
  </ul>
  <p class="mission-close">and ultimately improve emergency patient care for all Canadians.</p>

  <div class="contact">
    <p class="contact-label">For more information contact</p>
    <p class="contact-email">mdellow@brtl.ca</p>
  </div>

  <div class="group-photo" role="img" aria-label="Group photo of the alliance's researchers gathered in a meeting room"></div>

  <p class="site-url">www.brtl.ca</p>
</main>
</body>
</html>
```